Hotel Company Personal Business Card

This is a hotel business, personal business card. Need it sleek, professional, and sharp looking. I have a design attached that we can work with. My turnaround time is April 8th. I would need the cards by then. One side only color, the other side all details. This is flexible depending on the designs you come up with. I would like a boutique, unique, modern type of touch to the business card. Memorable type of card that people will want to keep.

Target Market(s)

Business professionals

Industry/Entity Type

Hospitality/Hotels & Resorts

Contact Information for Business Card

Name, email, phone number, address, and company name. Anything unique

Font styles to use
Serif
Sans Serif

Colors

Designer to choose colors to be used in the design.

Requirements
Nice to have
• Neutral colors. Eye popping logo. Sleek design. Boutique feel. Hint of color.

```html
<!DOCTYPE html>
<html lang="en">
<head>
<meta charset="utf-8">
<title>Harbor Crest Hotel Group – Business Card</title>
<link rel="stylesheet" href="https://fonts.googleapis.com/css2?family=Josefin+Sans:wght@400&family=Montserrat:wght@300;400&family=Lato:wght@400;700&display=swap">
<style>
  :root {
    --backdrop: #857e73;
    --gold-light: #8a7250;
    --gold-dark: #64502f;
    --charcoal: #2f3032;
    --charcoal-deep: #222326;
    --cream: #ded1c0;
    --bronze: #6b5a45;
    --ink: #1f1f22;
    --white: #ffffff;
  }
  * { margin: 0; padding: 0; box-sizing: border-box; }
  html, body {
    width: 1200px; height: 1000px; overflow: hidden;
    background: var(--backdrop);
  }
  .canvas { position: relative; width: 1200px; height: 1000px; }

  .card {
    position: absolute; left: 195px; width: 810px; height: 462px;
    border-radius: 0 22px 0 22px; overflow: hidden;
  }

  /* Front */
  .card--front { top: 29px; background: var(--charcoal-deep); }
  .front__band-top {
    position: absolute; left: 0; top: 0; width: 100%; height: 219px;
    background: radial-gradient(ellipse at 55% 20%, var(--gold-light) 0%, #7c6544 55%, var(--gold-dark) 100%);
  }
  .front__band-bottom {
    position: absolute; left: 0; top: 219px; width: 100%; height: 243px;
    background: radial-gradient(ellipse at 50% 35%, #37383a 0%, var(--charcoal) 40%, var(--charcoal-deep) 100%);
  }
  .front__peak { position: absolute; left: 243px; top: 68px; width: 324px; height: 151px; }
  .front__brand {
    position: absolute; left: 0; top: 295px; width: 100%;
    text-align: center; color: var(--white);
    font-family: "Josefin Sans", sans-serif; font-weight: 400;
    font-size: 44px; letter-spacing: 1px;
  }

  /* Back */
  .card--back { top: 509px; background: var(--cream); }
  .back__peak-top { position: absolute; left: 308px; top: 0; width: 194px; height: 92px; }
  .back__peak-bottom { position: absolute; left: 333px; top: 396px; width: 144px; height: 66px; }

  .person { position: absolute; left: 0; top: 128px; width: 100%; text-align: center; }
  .person__name {
    font-family: "Montserrat", sans-serif; font-weight: 300;
    font-size: 37px; letter-spacing: 1px; color: var(--ink); line-height: 1.1;
  }
  .person__name-first { color: var(--bronze); }
  .person__title {
    font-family: "Lato", sans-serif; font-weight: 700; font-size: 20px;
    color: var(--bronze); margin-top: 2px;
  }
  .divider { position: absolute; left: 303px; top: 207px; width: 204px; height: 18px; }

  .contact {
    position: absolute; left: 0; top: 242px; width: 100%;
    font-family: "Lato", sans-serif; font-size: 21px; color: var(--ink);
  }
  .contact__row {
    display: flex; justify-content: center; align-items: flex-start;
    gap: 12px; line-height: 25px; margin-bottom: 9px;
  }
  .contact__icon { width: 22px; height: 22px; flex: none; margin-top: 2px; }
  .contact__text--address { text-align: left; }
</style>
</head>
<body>
<main class="canvas">

  <section class="card card--front">
    <div class="front__band-top"></div>
    <div class="front__band-bottom"></div>
    <svg class="front__peak" viewBox="0 0 324 151" role="img" aria-label="Striped diamond motif">
      <defs>
        <linearGradient id="peakFill" x1="0" y1="0" x2="1" y2="0">
          <stop offset="0" stop-color="#3a3126"/>
          <stop offset="0.5" stop-color="#57462f"/>
          <stop offset="1" stop-color="#3a3126"/>
        </linearGradient>
      </defs>
      <polygon points="162,0 324,151 0,151" fill="#222326"/>
      <polygon points="162,14 306,151 18,151" fill="url(#peakFill)"/>
    </svg>
    <div class="front__brand">Harbor Crest Hotel Group</div>
  </section>

  <section class="card card--back">
    <svg class="back__peak-top" viewBox="0 0 194 92" role="img" aria-label="Striped diamond motif">
      <polygon points="0,0 194,0 97,92" fill="#222326"/>
      <polygon points="16,0 178,0 97,77" fill="#5a4a33"/>
    </svg>

    <div class="person">
      <div class="person__name"><span class="person__name-first">DANIEL</span> MOREAU</div>
      <div class="person__title">CEO</div>
    </div>

    <svg class="divider" viewBox="0 0 204 18">
      <line x1="0" y1="9" x2="204" y2="9" stroke="#2f3032" stroke-width="1.2"/>
      <rect x="82" y="2" width="40" height="14" rx="7" fill="#3a3530" role="img" aria-label="Scroll ornament"/>
    </svg>

    <div class="contact">
      <div class="contact__row">
        <svg class="contact__icon" viewBox="0 0 22 22" aria-hidden="true">
          <rect width="22" height="22" rx="3" fill="#5c4a33"/>
          <path d="M7 5.5l2.2 2.6-1.3 1.4c.8 1.7 2 2.9 3.6 3.7l1.4-1.3 2.6 2.2-1.3 2c-4.6-.5-8.4-4.3-8.9-8.9z" fill="#fff"/>
        </svg>
        <span class="contact__text">044-555 010 234</span>
      </div>
      <div class="contact__row">
        <svg class="contact__icon" viewBox="0 0 22 22" aria-hidden="true">
          <rect width="22" height="22" rx="3" fill="#5c4a33"/>
          <path d="M4.5 10.5L17 5l-3 12-3.5-3.5L9 16v-3.8z" fill="#fff"/>
        </svg>
        <span class="contact__text">info@harborcrest.com</span>
      </div>
      <div class="contact__row">
        <svg class="contact__icon" viewBox="0 0 22 22" aria-hidden="true">
          <rect width="22" height="22" rx="3" fill="#5c4a33"/>
          <path d="M11 3.5a5 5 0 0 1 5 5c0 3.6-5 10-5 10s-5-6.4-5-10a5 5 0 0 1 5-5z" fill="#fff"/>
          <circle cx="11" cy="8.6" r="1.9" fill="#5c4a33"/>
        </svg>
        <span class="contact__text contact__text--address">4471 Seabrook Bay Blvd<br>Blvd, 210-C, FL 32460</span>
      </div>
    </div>

    <svg class="back__peak-bottom" viewBox="0 0 144 66" role="img" aria-label="Striped diamond motif">
      <polygon points="72,0 144,66 0,66" fill="#222326"/>
      <polygon points="72,12 131,66 13,66" fill="#5a4a33"/>
    </svg>
  </section>

</main>
</body>
</html>
```